Thornvale plumbing business cards

Want a functional designed for my business cards using my logo

Company Name- Thornvale Plumbing, Heating & Water Systems
Name- Martin Thornvale
Title- Vice President
Cell- 555-318-7742
Email- Thornvaleplumbing@mailbrook.example
Business address-
PO Box 57
Jarrettsville, MD 21990

Plumbing

```html
<!DOCTYPE html>
<html lang="en">
<head>
<meta charset="utf-8">
<title>Thornvale Plumbing Business Cards</title>
<link rel="stylesheet" href="https://fonts.googleapis.com/css2?family=Open+Sans:wght@400;600&family=Roboto:wght@400;500;700&display=swap">
<style>
  :root {
    --page: #e9e6e2;
    --card-dark: #1d1e20;
    --brand-blue: #0a6cb8;
    --edge-blue: #8fb4e6;
    --text-light: #e3ecf7;
    --text-white: #ffffff;
    --text-muted: #8c9096;
  }
  * { margin: 0; padding: 0; box-sizing: border-box; }
  html, body {
    width: 1125px; height: 1200px; overflow: hidden;
    background: var(--page);
  }
  .canvas { position: relative; width: 1125px; height: 1200px; }
  .card {
    position: absolute; left: 150px; width: 824px; height: 470px;
    background: var(--card-dark); overflow: hidden;
    box-shadow: 0 6px 18px rgba(0,0,0,0.25);
  }
  .card--front { top: 98px; }
  .card--back { top: 630px; }
  .card__shapes { position: absolute; inset: 0; }
  .contact {
    position: absolute; left: 40px; top: 104px;
    font-family: "Roboto", sans-serif; color: var(--text-light);
  }
  .contact__name { font-size: 29px; font-weight: 700; color: var(--text-light); line-height: 1.1; }
  .contact__title { font-size: 19px; font-weight: 500; margin-top: 2px; }
  .contact__list { list-style: none; margin-top: 24px; font-size: 17px; line-height: 26px; }
  .contact__item { display: flex; align-items: flex-start; gap: 9px; }
  .contact__item--gap { margin-top: 10px; }
  .contact__icon { width: 18px; height: 18px; margin-top: 4px; flex: none; fill: var(--text-light); }
  .brand {
    position: absolute; left: 460px; width: 364px; top: 246px;
    text-align: center; font-family: "Open Sans", sans-serif; color: var(--text-white);
  }
  .brand__name { font-size: 33px; font-weight: 400; line-height: 1.1; }
  .brand__tagline { font-size: 21px; font-weight: 400; margin-top: 4px; }
  .back-brand {
    position: absolute; left: 0; right: 0; top: 170px; text-align: center;
    font-family: "Open Sans", sans-serif; font-size: 52px; font-weight: 400;
    color: var(--edge-blue);
  }
  .back-web {
    position: absolute; left: 0; right: 0; top: 388px; text-align: center;
    font-family: "Roboto", sans-serif; font-size: 19px; letter-spacing: 7px;
    color: var(--text-muted);
  }
</style>
</head>
<body>
<main class="canvas">
  <section class="card card--front">
    <svg class="card__shapes" width="824" height="470" viewBox="0 0 824 470" aria-hidden="true">
      <polygon points="0,0 479,0 335,175 489,470 0,470" fill="var(--brand-blue)"/>
      <polyline points="493,0 346,175 503,470" fill="none" stroke="var(--edge-blue)" stroke-width="6"/>
    </svg>
    <div class="contact">
      <h1 class="contact__name">Martin Thornvale</h1>
      <p class="contact__title">Vice President</p>
      <ul class="contact__list">
        <li class="contact__item">
          <svg class="contact__icon" viewBox="0 0 24 24"><path d="M12 2a7 7 0 0 0-7 7c0 5 7 13 7 13s7-8 7-13a7 7 0 0 0-7-7zm0 9.5A2.5 2.5 0 1 1 12 6.5a2.5 2.5 0 0 1 0 5z"/></svg>
          <span>PO Box 57<br>Cedar Hollow, PA 21990</span>
        </li>
        <li class="contact__item contact__item--gap">
          <svg class="contact__icon" viewBox="0 0 24 24"><path d="M6.6 10.8a15 15 0 0 0 6.6 6.6l2.2-2.2a1 1 0 0 1 1-.25 11.4 11.4 0 0 0 3.6.6 1 1 0 0 1 1 1V20a1 1 0 0 1-1 1A17 17 0 0 1 3 4a1 1 0 0 1 1-1h3.5a1 1 0 0 1 1 1c0 1.25.2 2.450.6 3.6a1 1 0 0 1-.25 1z"/></svg>
          <span>555-204-6631</span>
        </li>
        <li class="contact__item">
          <svg class="contact__icon" viewBox="0 0 24 24"><path d="M7 1h10a2 2 0 0 1 2 2v18a2 2 0 0 1-2 2H7a2 2 0 0 1-2-2V3a2 2 0 0 1 2-2zm0 3v14h10V4zm5 15.5a1 1 0 1 0 0 2 1 1 0 0 0 0-2z"/></svg>
          <span>555-318-7742</span>
        </li>
        <li class="contact__item">
          <svg class="contact__icon" viewBox="0 0 24 24"><path d="M3 5h18v14H3zm2 2v.5l7 5 7-5V7l-7 5z"/></svg>
          <span>Thornvaleplumbing@mailbrook.example</span>
        </li>
        <li class="contact__item">
          <svg class="contact__icon" viewBox="0 0 24 24"><path d="M12 2a10 10 0 1 0 0 20 10 10 0 0 0 0-20zm-1 17.9A8 8 0 0 1 4.1 10.9L9 15.8v1a2 2 0 0 0 2 2zm6.9-2.5A2 2 0 0 0 16 16h-1v-3a1 1 0 0 0-1-1H8v-2h2a1 1 0 0 0 1-1V7h2a2 2 0 0 0 2-2v-.4a8 8 0 0 1 2.9 12.8z"/></svg>
          <span>www.Thornvaleplumbing.com</span>
        </li>
      </ul>
    </div>
    <div class="brand">
      <p class="brand__name">Thornvale Plumbing</p>
      <p class="brand__tagline">Heating &amp; Water Systems</p>
    </div>
  </section>

  <section class="card card--back">
    <p class="back-brand">Thornvale Plumbing</p>
    <p class="back-web">www.Thornvaleplumbing.com</p>
  </section>
</main>
</body>
</html>
```